Web Banner Ads needed for conference production company

We are a company that puts on conferences and trainings around the US. We are looking for a talented Graphic Designer who can create a web banner ad to help us promote a social media ebook.
We need banner ads in the following sizes: 160x600, 336x280, 300x250, 728x90
Please reference the social media eBook landing page for colors and fonts: http://learning-center.brightwaveforumseries.example/sm-ebook/
You can also reference our event website: http://www.brightwaveforumseries.example
Fonts don't need to be exact but we would like it similar enough to be clearly identifiable with the landing page.
Content on the ad MUST include:
40 Standout Firms Winning Online Crowds
Download Free eBook Now
brought to you by KTVR
- please include KTVR logo, attached.
- please include social media globe if able, attached.
CEOs, CMOs, Directors and Managers of Marketing & Business Development, Executives & Business Professionals.

```html
<!DOCTYPE html>
<html lang="en">
<head>
<meta charset="utf-8">
<title>KTVR eBook Banner 160x600</title>
<link rel="stylesheet" href="https://fonts.googleapis.com/css2?family=Ubuntu:wght@500;700&display=swap">
<style>
  :root {
    --page: #ffffff;
    --banner-bg: #1b4858;
    --banner-bg-deep: #143a48;
    --headline-top: #ffd23a;
    --headline-bottom: #f7941d;
    --headline-outline: #1a1a1a;
    --brands-yellow: #ffd45c;
    --ink: #0a0a0a;
    --now-blue: #cfe6ea;
    --glow: #ffe34d;
    --mark-blue: #3a9fd6;
    --mark-white: #ffffff;
    --globe-light: #eef4f8;
    --globe-mid: #9fb7c9;
    --globe-edge: #5d7c93;
  }
  * { margin: 0; padding: 0; box-sizing: border-box; }
  html, body {
    width: 1200px; height: 1000px; overflow: hidden;
    background: var(--page);
  }
  .canvas { position: relative; width: 1200px; height: 1000px; }
  .banner {
    position: absolute; left: 520px; top: 200px;
    width: 160px; height: 600px; overflow: hidden;
    background: linear-gradient(180deg, var(--banner-bg) 0%, var(--banner-bg-deep) 100%);
    font-family: "Ubuntu", sans-serif;
    text-align: center;
  }
  .banner__glow {
    position: absolute; left: -20px; top: 230px; width: 200px; height: 110px;
    background: radial-gradient(ellipse at 50% 45%, var(--glow) 0%, rgba(255,170,30,.6) 25%, rgba(255,170,30,0) 65%);
  }
  .headline-number {
    position: absolute; left: 0; right: 0; top: 2px;
    font-size: 112px; font-weight: 700; line-height: 1; letter-spacing: -4px;
    background: linear-gradient(180deg, var(--headline-top), var(--headline-bottom));
    -webkit-background-clip: text; background-clip: text; color: transparent;
    -webkit-text-stroke: 2px var(--headline-outline);
  }
  .headline-word {
    position: absolute; left: 0; right: 0; top: 96px;
    font-size: 23px; font-weight: 700; line-height: 1; color: var(--headline-top);
    -webkit-text-stroke: 1px var(--headline-outline); paint-order: stroke fill;
  }
  .headline-noun {
    position: absolute; left: 0; right: 0; top: 119px;
    font-size: 31px; font-weight: 700; line-height: 1; color: var(--brands-yellow);
    -webkit-text-stroke: 1.5px var(--headline-outline); paint-order: stroke fill;
  }
  .globe {
    position: absolute; left: 6px; top: 146px; width: 148px; height: 148px;
    border-radius: 50%;
    background: radial-gradient(circle at 40% 38%, var(--globe-light) 0%, var(--globe-mid) 60%, var(--globe-edge) 100%);
  }
  .cta-download {
    position: absolute; left: 0; right: 0; top: 298px;
    font-size: 30px; font-weight: 700; line-height: 1; color: var(--ink);
  }
  .cta-offer {
    position: absolute; left: 0; right: 0; top: 334px;
    font-size: 20px; font-weight: 700; line-height: 1; color: var(--ink);
  }
  .cta-now {
    position: absolute; left: 0; right: 0; top: 346px;
    font-size: 64px; font-weight: 700; line-height: 1; color: var(--now-blue);
    letter-spacing: -1px;
  }
  .credit {
    position: absolute; left: 0; right: 0; top: 408px;
    font-size: 16px; font-weight: 700; line-height: 17px; color: var(--ink);
  }
  .sponsor {
    position: absolute; left: 10px; top: 450px; width: 140px; height: 136px;
    display: flex; align-items: center; justify-content: center; gap: 8px;
  }
  .sponsor__square { width: 22px; height: 22px; background: var(--mark-blue); }
  .sponsor__name {
    font-size: 38px; font-weight: 700; line-height: 1; color: var(--mark-white);
  }
</style>
</head>
<body>
<main class="canvas">
  <section class="banner" aria-label="Free eBook banner">
    <div class="banner__glow"></div>
    <div class="headline-number">40</div>
    <div class="headline-word">standout</div>
    <div class="headline-noun">FIRMS</div>
    <div class="globe" role="img" aria-label="Globe covered in tiles of social media app icons"></div>
    <div class="cta-download">download</div>
    <div class="cta-offer">FREE EBOOK</div>
    <div class="cta-now">now</div>
    <p class="credit">brought to you<br>by KTVR</p>
    <div class="sponsor" aria-label="KTVR">
      <span class="sponsor__square"></span>
      <span class="sponsor__name">KTVR</span>
    </div>
  </section>
</main>
</body>
</html>
```